Clean book cover design for book about writing a book

Book title: The Crossing
Subtitle: 9 Paths to Crafting a Volume that Counts
Name: Marisol T. Brenwick, The Quill Nursery

This is a book which teaches 10 steps to writing a self-help book. I'm looking for a very clean impactful cover either with no image or just a small simple image of a book, typewriter, laptop, cabin or something very simple. I am attaching the manuscript here if reading it would help you with the cover. The theme of the book is that you can write with joy and ease and your book can just flow out of you if you learn how to clear the blocks between you and your book already written. Sort of a new agey stance on book writing.

The book should generally match the branding on my website. Www.TheQuillNursery.example.

I have photos of myself attached which I'd like used for the back cover with an "about the author section of maybe 50 words.

The project is for the full back cover and spine as well as the front cover (see print Forge template attached) but to win the contest you can just design the front cover and then I'll give the winner the template for the full design with the back cover copy. Or you can design the full cover using the template and you can use Loren ipsum text if you need to.

My clients are very upmarket and the themes of my business revolve around nuturing and incubating ideas and authors. Very feminine creation energy.

For colors see The Crossing Press (CB) wax seals and the background fades. I don't want my logo on the cover but I am attaching it here so you get a feel for the branding. The logo is in the LOBSTER font and you can see how we do the grey with the rainbow shadow.

Here are some covers I like:

http://www.shopvale.example/Pen-Tome-Quick-Stage---Stage/dp/055817342Q
http://www.shopvale.example/Plotting-Your-Tale-Chart-Triumph/dp/0841739265
http://www.shopvale.example/Be-Scribe-Seeking-Voice-Guide-ebook/dp/K22R9WQ3L1
http://www.shopvale.example/Strays-Tale-Triumph-Rupert-Vanhollow/dp/0552048871
Updates

I have revised my brief to include some picture and images that will help you create the cover. I have also included some of my favorite covers to give you more of a sense of what I'm going for. And I have included the manuscript in case it would help you to skim through it in order to get a sense of the reader and the book. I think if you look at my revised brief it will make it easier to create a submission. Thanks!

Target Market(s)

Women 40-60 who run small businesses as life coaches or other healing jobs (therapy, reiki, light work) they have a spiritual/new age bent.

Industry/Entity Type

Business

Font styles to use
Serif
Other font styles liked:
• Lobster (not required... just a suggestion since it's my logo font)

Requirements
Must have
• Name and title easy to read in 1" x 1" thumb nail
Nice to have
• Fantastic type face treatment.

Match the look and feel of my website.
Should not have
• Busy images. With one simple image or just designed with colors and typeface treatment

```html
<!DOCTYPE html>
<html lang="en">
<head>
<meta charset="utf-8">
<title>The Crossing — Book Cover</title>
<link rel="stylesheet" href="https://fonts.googleapis.com/css2?family=Comfortaa:wght@300&family=Cabin+Condensed:wght@400&family=Architects+Daughter&display=swap">
<style>
  :root {
    --backdrop: #b8b8b8;
    --paper: #ffffff;
    --burgundy: #6a0a0c;
    --banner-red: #ea2129;
    --banner-text: #ffffff;
    --ink-grey: #3a3a3a;
    --books-warm: #c9442a;
    --books-cool: #7fa6d6;
  }
  html, body {
    margin: 0;
    padding: 0;
    width: 1200px;
    height: 1200px;
    overflow: hidden;
    background: var(--backdrop);
  }
  .canvas {
    position: relative;
    width: 1200px;
    height: 1200px;
    display: flex;
    align-items: center;
    justify-content: center;
  }
  .cover {
    position: relative;
    width: 700px;
    height: 1060px;
    background: var(--paper);
    box-shadow: 0 6px 24px rgba(0,0,0,0.18);
  }
  .title {
    position: absolute;
    left: 0;
    right: 0;
    top: 80px;
    margin: 0;
    font-family: "Comfortaa", sans-serif;
    font-weight: 300;
    color: var(--burgundy);
    line-height: 1;
  }
  .title-lead {
    display: block;
    font-size: 150px;
    padding-left: 210px;
    letter-spacing: -2px;
  }
  .title-main {
    display: block;
    font-size: 124px;
    text-align: center;
    margin-top: -10px;
    letter-spacing: -1px;
  }
  .subtitle {
    position: absolute;
    left: 38px;
    right: 38px;
    top: 438px;
    margin: 0;
    padding: 8px 0 9px;
    background: var(--banner-red);
    border-radius: 12px;
    color: var(--banner-text);
    font-family: "Cabin Condensed", sans-serif;
    font-size: 31px;
    text-align: center;
    white-space: nowrap;
  }
  .book-stack {
    position: absolute;
    left: 200px;
    top: 540px;
    width: 300px;
    height: 180px;
    border-radius: 6px;
    background: linear-gradient(100deg, var(--books-cool) 0%, #e6e6e6 45%, var(--books-warm) 70%, #4a4a4a 100%);
    opacity: 0.85;
  }
  .byline {
    position: absolute;
    left: 0;
    right: 0;
    bottom: 120px;
    text-align: center;
  }
  .author {
    margin: 0;
    font-family: "Architects Daughter", cursive;
    font-size: 42px;
    color: var(--ink-grey);
  }
  .imprint {
    margin: 6px 0 0;
    font-family: "Cabin Condensed", sans-serif;
    font-size: 24px;
    color: var(--ink-grey);
  }
</style>
</head>
<body>
  <main class="canvas">
    <article class="cover">
      <h1 class="title">
        <span class="title-lead">The</span>
        <span class="title-main">Crossing</span>
      </h1>
      <p class="subtitle">9 Paths to Crafting a Volume that Counts</p>
      <div class="book-stack" role="img" aria-label="Illustration of a row of colourful books toppling like dominoes"></div>
      <footer class="byline">
        <p class="author">Marisol T. Brenwick</p>
        <p class="imprint">The Quill Nursery</p>
      </footer>
    </article>
  </main>
</body>
</html>
```